Upsell Vertical Banner Ad Design For B2B Marketing Agency Vertical 768px × 1180px IS THE SIZE

I need a banner made for my website www.brightlanepromotionhub.biz This banner will be an upsell advertisement for after someone signs up for my monthly program. When they login to their account for the 1st time I will give them the chance to upgrade their account to our annual program with just one click.

this is a page that upsells it currently to give you an idea how we market ourselves:
https://tlpx.pagevault-example.com/page/tlp-annual-upsell

Use this content:

Are You Ready To Commit To Taking Your Business To The Next Level?

Because We're In This For The Long-Haul and Dedicated To Your Success...

Save $300 By Upgrading To An Annual Membership And Pay Only $74/mth

((BUTTON))Yes, Upgrade My Plan Right Now!

*Must prepay the full year at only $898/yr!

Target Market(s)

business owners

Industry/Entity Type

Marketing

Requirements
Must have
• 768px × 1180px IS THE SIZE vertical

Use this content:

Nice to have
• Use this content:

Should not have
• Use this content:

```html
<!DOCTYPE html>
<html lang="en">
<head>
<meta charset="utf-8">
<title>Bright Lane Promotion Hub – Annual Upgrade</title>
<link rel="stylesheet" href="https://fonts.googleapis.com/css2?family=Montserrat:wght@600;700&family=Lato:wght@300;400;700;900&display=swap">
<style>
  :root {
    --ink: #1c1c1c;
    --ink-soft: #2a2a2a;
    --muted: #6a6a6a;
    --green: #00ad50;
    --white: #ffffff;
    --hero-deep: #1e5a7a;
    --hero-mid: #3f8f9c;
    --hero-light: #6fb7a8;
  }
  html, body {
    margin: 0;
    padding: 0;
    width: 781px;
    height: 1200px;
    overflow: hidden;
    background: var(--white);
  }
  .banner {
    width: 768px;
    height: 1180px;
    position: relative;
    transform: scale(1.0169);
    transform-origin: 0 0;
    background: var(--white);
    font-family: "Lato", sans-serif;
  }
  .hero {
    position: absolute;
    inset: 0 0 auto 0;
    height: 428px;
    background:
      radial-gradient(ellipse at 75% 70%, rgba(120,190,170,0.55), transparent 60%),
      radial-gradient(ellipse at 20% 20%, rgba(40,100,140,0.7), transparent 60%),
      linear-gradient(160deg, var(--hero-deep) 0%, var(--hero-mid) 50%, var(--hero-light) 100%);
    clip-path: polygon(0 0, 100% 0, 100% 338px, 50% 428px, 0 338px);
  }
  .hero-shade {
    position: absolute;
    left: 0; right: 0; top: 338px;
    height: 110px;
    background: linear-gradient(#f2f2f2, rgba(255,255,255,0));
    clip-path: polygon(0 0, 50% 90px, 100% 0, 100% 100%, 0 100%);
    opacity: 0.6;
  }
  .brand {
    position: absolute;
    top: 142px;
    left: 0; right: 0;
    display: flex;
    justify-content: center;
    align-items: center;
    gap: 16px;
    color: var(--white);
    font-family: "Montserrat", sans-serif;
    font-weight: 700;
    font-size: 30px;
    letter-spacing: 1px;
  }
  .brand-dot {
    width: 44px;
    height: 44px;
    border-radius: 50%;
    background: var(--white);
  }
  .headline {
    position: absolute;
    top: 482px;
    left: 20px; right: 20px;
    margin: 0;
    text-align: center;
    font-family: "Montserrat", sans-serif;
    font-weight: 700;
    font-size: 40px;
    line-height: 61px;
    letter-spacing: 0.6px;
    color: var(--ink);
  }
  .subline {
    position: absolute;
    top: 700px;
    left: 60px; right: 80px;
    margin: 0;
    text-align: center;
    font-weight: 400;
    font-size: 28px;
    line-height: 44px;
    color: var(--muted);
  }
  .offer {
    position: absolute;
    top: 806px;
    left: 40px; right: 40px;
    margin: 0;
    text-align: center;
    font-weight: 700;
    font-size: 34px;
    line-height: 54px;
    color: var(--ink-soft);
  }
  .offer .price { color: var(--green); }
  .offer .price-big { font-size: 40px; }
  .cta {
    position: absolute;
    top: 955px;
    left: 111px;
    width: 547px;
    height: 81px;
    border-radius: 8px;
    background: var(--green);
    color: var(--white);
    display: flex;
    align-items: center;
    justify-content: center;
    font-weight: 900;
    font-size: 25px;
    text-decoration: none;
    letter-spacing: 0.2px;
  }
  .terms {
    position: absolute;
    top: 1070px;
    left: 0; right: 0;
    margin: 0;
    text-align: center;
    font-weight: 700;
    font-size: 24px;
    color: var(--ink-soft);
  }
  .terms .price { color: var(--green); }
</style>
</head>
<body>
  <main class="banner">
    <div class="hero" role="img" aria-label="Aerial city skyline along a river overlaid with teal stock-chart grid lines"></div>
    <div class="hero-shade"></div>
    <div class="brand">
      <span class="brand-dot"></span>
      <span class="brand-name">BRIGHT LANE PROMOTION HUB</span>
    </div>

    <h1 class="headline">ARE YOU READY TO COMMIT<br>TO TAKING YOUR BUSINESS TO<br>THE NEXT LEVEL?</h1>

    <p class="subline">Because We're In This For The Long-Haul and Dedicated To Your Success...</p>

    <p class="offer">Save <span class="price price-big">$300</span> By Upgrading To An Annual<br>Membership And Pay Only <span class="price">$74/mth</span></p>

    <a class="cta" href="https://tlpx.pagevault-example.com/page/tlp-annual-upsell">YES, UPGRADE MY PLAN RIGHT NOW!</a>

    <p class="terms">Must prepay the full year at only <span class="price">$898/yr!</span></p>
  </main>
</body>
</html>
```